Poem Handwritten by Veteran while in the jungle of Vietnam

My parents are celebrating their 50th wedding anniversary this year. I wanted to give them a very memorable gift. On my parents 2nd anniversary, my father was stationed in Vietnam. On that night he was in the jungle waiting till morning and wrote a poem to my mother using his pant leg as paper. I would like this poem to typographically designed to be framed and hung on the wall.

I have attached a picture of the poem below. It will need to be 11x14 when printed for framing. It would be great if there was background or artwork to make it more visually interesting, perhaps in a watercolor. My parents have a transitional style. I have attached some possible color schemes as well. Cool greens, blue, neutral grays, with hints of berries or highlights of yellow. These are just a guide, I would be open to your interpretations.

Thank you for your help. This will hopefully be a gift they will truly treasure as much as the poem itself.

Target Market(s)

My parents who are excited to be celebrating their 50th wedding anniversary. It should have a transitional, mature style.

Font styles to use
Serif
Script

Requirements
Must have
• The poem, typographically designed. There can be a mix of fonts, but legibility is critically important.
• Now that some designs have come through I wanted to give some more guidance of what I'm looking for. I want something that feels sophisticated and artistic.
Nice to have
• A background or art work, using the color schemes attached as a guide. I am really liking the designs that have a full color landscape artwork in the background. The fonts should be elegant and formal. I really like the romantic, muted colors. I had trouble finding similar projects online in the style I wanted until I cam across wedding invites. Those seem to be the most applicable. I've added pictures of some so you can get a sense of what I'm looking for. I am really liking the jungle foliage, starry skies or sunrises.
Should not have
• Cartoon caricatures, fonts that are too illegible when printed. I'm not liking anything whimsical. I don't like the very bright colors for this project.

```html
<!DOCTYPE html>
<html lang="en">
<head>
<meta charset="utf-8">
<title>Happy Anniversary Darling</title>
<link rel="stylesheet" href="https://fonts.googleapis.com/css2?family=Pinyon+Script&family=Crimson+Text:ital@0;1&display=swap">
<style>
  :root {
    --backdrop: #5b5b5b;
    --night: #0b0a0a;
    --rose-deep: #6e0710;
    --rose: #a10f1c;
    --rose-light: #c8202c;
    --band: rgba(150, 8, 20, 0.62);
    --panel-top: rgba(150, 14, 24, 0.88);
    --panel-bottom: #5a0710;
    --ink: #fbf3f0;
  }
  * { margin: 0; padding: 0; box-sizing: border-box; }
  html, body { width: 1200px; height: 1200px; overflow: hidden; }
  body { background: var(--backdrop); position: relative; }

  .poster {
    position: absolute; left: 225px; top: 102px;
    width: 785px; height: 999px;
    background: var(--night);
    overflow: hidden;
  }
  .poster__artwork {
    position: absolute; inset: 0;
    background:
      radial-gradient(ellipse 260px 200px at 170px 210px, var(--rose) 0%, rgba(110,7,16,0.6) 55%, transparent 100%),
      radial-gradient(ellipse 260px 220px at 620px 200px, var(--rose) 0%, rgba(110,7,16,0.6) 55%, transparent 100%),
      radial-gradient(ellipse 330px 160px at 400px 340px, var(--rose-deep) 0%, transparent 100%),
      radial-gradient(ellipse 160px 260px at 720px 460px, rgba(110,7,16,0.7) 0%, transparent 100%),
      radial-gradient(ellipse 120px 220px at 40px 480px, rgba(110,7,16,0.6) 0%, transparent 100%),
      linear-gradient(180deg, #111612 0%, #140a0b 45%, var(--night) 75%);
  }
  .title-band {
    position: absolute; left: 0; top: 64px;
    width: 100%; height: 226px;
    background: var(--band);
  }
  .title {
    position: absolute; left: 0; top: 108px; width: 100%;
    text-align: center;
    font-family: "Pinyon Script", cursive;
    color: var(--ink);
    font-size: 76px; line-height: 72px;
    text-shadow: 2px 3px 4px rgba(40, 0, 0, 0.7);
  }
  .title span { display: block; }
  .title__second { padding-left: 20px; }

  .poem-panel {
    position: absolute; left: 104px; top: 332px;
    width: 577px; height: 618px;
    background: linear-gradient(180deg, var(--panel-top) 0%, #7d0913 60%, var(--panel-bottom) 100%);
  }
  .poem-frame {
    position: absolute; left: 17px; top: 38px;
    width: 543px; height: 566px;
    border: 1.5px solid var(--ink);
    border-top: none;
  }
  .poem-frame__top {
    position: absolute; top: 0; height: 1.5px; background: var(--ink);
  }
  .poem-frame__top--left { left: 0; width: 126px; }
  .poem-frame__top--right { right: 0; width: 126px; }

  .poem-heading {
    position: absolute; left: 0; top: 23px; width: 100%;
    text-align: center;
    font-family: "Crimson Text", serif;
    font-size: 11.5px; line-height: 16px;
    letter-spacing: 0.2px;
    color: var(--ink);
  }

  .poem-column {
    position: absolute; top: 96px; width: 290px;
    text-align: center;
    font-family: "Crimson Text", serif;
    font-style: italic;
    font-size: 14.2px; line-height: 17.9px;
    color: var(--ink);
  }
  .poem-column--left { left: 17px; }
  .poem-column--right { left: 284px; }
  .stanza { margin-bottom: 17.9px; }
</style>
</head>
<body>
  <main class="poster">
    <div class="poster__artwork" role="img" aria-label="Dark red roses with dew drops on deep green foliage"></div>
    <div class="title-band"></div>
    <h1 class="title">
      <span class="title__first">Happy Anniversary</span>
      <span class="title__second">Darling</span>
    </h1>

    <section class="poem-panel">
      <div class="poem-frame">
        <div class="poem-frame__top poem-frame__top--left"></div>
        <div class="poem-frame__top poem-frame__top--right"></div>
      </div>
      <p class="poem-heading">20 July 1970, Monday, LZ Ridgeline<br>Walter’s Anniversary Poem</p>

      <div class="poem-column poem-column--left">
        <p class="stanza">Life’s journey began with a challenge,<br>It was heralded far and near.<br>The road led forever,<br>Its completion was known to be dear.</p>
        <p class="stanza">From the garden of light it proceeded,<br>To the valley of shadows it led.<br>Thorns and thistles adorned it,<br>Past abyss and crevice is sped.</p>
        <p class="stanza">The brave surged forward with courage,<br>The wise undaunted pressed on.<br>The mighty held high their banner,<br>We all awaited the dawn.</p>
        <p class="stanza">Though the pitfalls and hazards were many,<br>The pathway was clear in view.<br>Straight and sure it glided,<br>Its course we knew to be true.</p>
        <p class="stanza">I knew you, Sweetheart, beforehand,<br>So precious and sweet were you,<br>Our moments of bliss were priceless,<br>Each day brought us joy anew.</p>
        <p class="stanza">The call to progression beckoned,<br>At last I would have my chance–</p>
      </div>

      <div class="poem-column poem-column--right">
        <p class="stanza">To clasp you to me forever,<br>And seal our divine romance.</p>
        <p class="stanza">I eagerly started the journey,<br>Though with sorrow, I left you behind.<br>With courage and faith I continued,<br>For I knew, that you later I’d find.</p>
        <p class="stanza">I diligently search for you, Darling,<br>The roadway was both bleak and fair.<br>Though the years grew long in number,<br>I did not give up in despair.</p>
        <p class="stanza">At last in the distance I saw you,<br>So beautiful, lovely, and sweet!<br>Your attention I struggled to capture,<br>Your love I wrested to meet.</p>
        <p class="stanza">What rapture was mine in fulfilment,<br>As now together we stand.<br>To cherish and love each other,<br>While our plans and dreams expand.</p>
        <p class="stanza">I love you, Darling, forever,<br>My life you have made replete.<br>Our eternal mansion beckons,<br>Your love has made it complete.</p>
      </div>
    </section>
  </main>
</body>
</html>
```